Investor Information Presentation Design Required and Corporate overview design

I have all the materials ready to go, just need 1x Pro Design for the presentation and 1x Pro Design for the corporate overview.
I am ok with images being changed (only if it represents the company better). Wording Can NOT be changed. Any process diagrams can be changed to better represent the process.
I can provide high res Logo file and obviously the files for the presentation and corporate overview. What I have done is basic, but need it to look far more polished and professional.

Target Market(s)

Fixed Term Deposits - $100,000 + High interest rates

Industry/Entity Type

Investment

Font styles to use
Sans Serif

Requirements
Must have
• A corporate professional look, think banks, financial services, business etc
• The presentation is NOT used for group presenting purposes - Individuals go through it on their own. Should want to make me feel like I have to read it all!

```html
<!DOCTYPE html>
<html lang="en">
<head>
<meta charset="utf-8">
<title>The Problem</title>
<link href="https://fonts.googleapis.com/css2?family=Montserrat:wght@800&family=Roboto:wght@300;400;500;700&display=swap" rel="stylesheet">
<style>
  :root {
    --header-bg: #e9e9ec;
    --page-bg: #ffffff;
    --footer-bg: #8b8a97;
    --blue: #29a3e0;
    --navy: #2b2a5e;
    --grey-text: #9c9ba8;
    --white: #ffffff;
    --photo-dark: #2a2a2d;
    --photo-mid: #8d8d92;
    --photo-light: #f1f1f1;
  }
  * { margin: 0; padding: 0; box-sizing: border-box; }
  html, body { width: 1200px; height: 900px; overflow: hidden; background: var(--page-bg); }
  .slide {
    position: relative;
    width: 1200px;
    height: 900px;
    background: var(--page-bg);
    font-family: 'Roboto', Arial, sans-serif;
  }
  .slide-header {
    position: absolute;
    left: 0; top: 0;
    width: 1200px; height: 117px;
    background: var(--header-bg);
  }
  .slide-title {
    position: absolute;
    left: 42px; top: 34px;
    font-family: 'Montserrat', Arial, sans-serif;
    font-weight: 800;
    font-size: 40px;
    letter-spacing: 0.5px;
    color: var(--navy);
  }
  .slide-title .accent { color: var(--blue); }
  .brand-name {
    position: absolute;
    right: 36px; top: 44px;
    display: flex; align-items: center; gap: 10px;
    font-family: 'Roboto', Arial, sans-serif;
    font-weight: 700;
    font-size: 22px;
    color: var(--navy);
  }
  .brand-name .mark {
    width: 14px; height: 14px;
    background: var(--blue);
    border-radius: 50%;
  }
  .point {
    position: absolute;
    left: 36px;
    display: flex;
    align-items: flex-start;
  }
  .point-marker {
    width: 44px; height: 44px;
    margin-top: 12px;
    margin-right: 34px;
    border-radius: 50%;
    background: var(--blue);
    flex-shrink: 0;
  }
  .point-text { color: var(--grey-text); font-weight: 400; font-size: 25px; line-height: 1.3; }
  .point-text .lead { display: block; }
  .point-text .emphasis { display: block; color: var(--blue); font-weight: 700; font-size: 29px; margin-top: 8px; }
  .point-text .inline-emphasis { color: var(--blue); font-weight: 700; font-size: 28px; }
  .point--rates { top: 212px; }
  .point--inflation { top: 407px; }
  .point--profit { top: 600px; }
  .hero-photo {
    position: absolute;
    left: 642px; top: 240px;
    width: 558px; height: 428px;
    background:
      radial-gradient(circle at 62% 58%, var(--photo-light) 0%, #d9d9db 38%, var(--photo-mid) 52%, var(--photo-dark) 62%, transparent 63%),
      var(--page-bg);
  }
  .slide-footer {
    position: absolute;
    left: 0; bottom: 0;
    width: 1200px; height: 36px;
    background: var(--footer-bg);
    color: var(--white);
    font-weight: 500;
    font-size: 16px;
    line-height: 36px;
    padding-left: 9px;
    letter-spacing: 0.3px;
  }
</style>
</head>
<body>
<div class="slide">
  <header class="slide-header">
    <h1 class="slide-title"><span class="accent">THE</span> PROBLEM</h1>
    <div class="brand-name"><span class="mark"></span>Harbourline</div>
  </header>

  <div class="point point--rates">
    <span class="point-marker"></span>
    <p class="point-text">
      <span class="lead">Term deposits with leading banks pay</span>
      <span class="emphasis">less than 4.0% per annum</span>
    </p>
  </div>

  <div class="point point--inflation">
    <span class="point-marker"></span>
    <p class="point-text">
      <span class="lead">Savings are getting</span>
      <span class="emphasis">eroded by inflation</span>
    </p>
  </div>

  <div class="point point--profit">
    <span class="point-marker"></span>
    <p class="point-text">
      <span class="lead">Banks <span class="inline-emphasis">continue to profit</span> despite</span>
      <span class="lead">paying low rates of return</span>
    </p>
  </div>

  <div class="hero-photo" role="img" aria-label="Photo of a silver stopwatch whose dial reads 'Time to Invest'"></div>

  <footer class="slide-footer">HARBOURLINE CAPITAL PTY LTD ACN: 000 111 222</footer>
</div>
</body>
</html>
```